" A Virtal Soluçoes Ambientais é uma empresa que presta serviços de regularizaçao ambiental. Trata-se de uma consultoria ambiental cujo principal serviço é oferecer soluçoes ambientais para atividades produtivas e imóveis urbanos ou rurais. Exemplos: (i) correçao de matrículas e registros em órgao públicos para fazendas produtivas; (ii) correçao de emissoes atmosféricas, ruídos, resíduos, etc, de indústrias; (iii) descontaminaçao do solo ou água subterrânea de um imóvel; (iv) elaboraçao de laudos técnicos sobre passivos ambientais. Observaçao importante: a empresa nao é uma ONG, embora o apelo seja ambiental. "

```html
<!DOCTYPE html>
<html lang="pt-BR">
<head>
<meta charset="utf-8">
<title>Virtal Soluçoes Ambientais – Cartão de visita</title>
<link href="https://fonts.googleapis.com/css2?family=Open+Sans:wght@400;600&display=swap" rel="stylesheet">
<style>
  :root {
    --backdrop: #e6e6e4;
    --card: #ffffff;
    --card-shade: #f2f2f0;
    --brand-slate: #2f4048;
    --accent-olive: #7d8a3c;
    --text-grey: #707070;
  }
  html, body {
    margin: 0;
    width: 1200px;
    height: 1200px;
    overflow: hidden;
    background: var(--backdrop);
  }
  .canvas {
    position: relative;
    width: 1200px;
    height: 1200px;
  }
  .business-card {
    position: absolute;
    left: 120px;
    top: 512px;
    width: 960px;
    height: 176px;
    background: linear-gradient(90deg, var(--card) 0%, var(--card) 55%, var(--card-shade) 100%);
    box-shadow: 0 2px 6px rgba(0,0,0,0.12);
    font-family: "Open Sans", sans-serif;
  }
  .wordmark {
    position: absolute;
    left: 62px;
    top: 52px;
    color: var(--brand-slate);
    font-weight: 400;
  }
  .wordmark-name {
    display: block;
    font-size: 78px;
    line-height: 1;
    letter-spacing: 2px;
  }
  .wordmark-tagline {
    display: block;
    margin-top: 6px;
    font-size: 13px;
    letter-spacing: 9.5px;
    text-transform: uppercase;
  }
  .contact {
    position: absolute;
    left: 650px;
    top: 14px;
    color: var(--text-grey);
    font-size: 11px;
    line-height: 1.35;
  }
  .contact-name {
    margin: 0 0 10px;
    color: var(--accent-olive);
    font-size: 19px;
    font-weight: 600;
  }
  .contact p {
    margin: 0 0 8px;
  }
  .contact-web {
    color: var(--accent-olive);
    margin-top: 12px !important;
  }
</style>
</head>
<body>
<main class="canvas">
  <section class="business-card">
    <div class="wordmark">
      <span class="wordmark-name">VIRTAL</span>
      <span class="wordmark-tagline">Soluções Ambientais</span>
    </div>
    <div class="contact">
      <h1 class="contact-name">Tiago Ramos Leal</h1>
      <p>tiago@virtalambiental.com.br<br>+55 11 90000 1234</p>
      <p>rua das palmeiras 240 2º andar pinheiros<br>05422 100 são paulo sp brasil<br>+55 11 3000 4500</p>
      <p class="contact-web">www.virtalambiental.com.br</p>
    </div>
  </section>
</main>
</body>
</html>
```